Building Servicess

We need a new business card design for a company. We specialise in: Electrical/Site temporary electrics, Data/Network Installation, Passive Fire Protection

Industry/Entity Type

Construction

Contact Information for Business Card

Services provided as detailed on project description

Font styles to use
Serif

Colors
0054AA
0677BA
7BADD7
CADEEF
E8F1F8
00AB8E
00BBA5
67D7C9
C6EFE9
E9F9F6
EB3D1F
EC4F4E
F09395
F8D3D4
FCEDEE

Requirements
Must have
• Company logo-contact details-phone numbers

```html
<!DOCTYPE html>
<html lang="en">
<head>
<meta charset="utf-8">
<title>Brightline Works – Business Cards</title>
<link href="https://fonts.googleapis.com/css2?family=Montserrat:wght@400;500;600&display=swap" rel="stylesheet">
<style>
  :root {
    --backdrop: #2b2b2e;
    --card-fill: #1c1c1e;
    --brand-blue: #1677c9;
    --brand-grey: #8a8a8c;
    --text-light: #f2f2f2;
  }
  * { margin: 0; padding: 0; box-sizing: border-box; }
  html, body {
    width: 1200px; height: 786px; overflow: hidden;
    background: var(--backdrop);
    font-family: "Montserrat", sans-serif;
  }
  .canvas { position: relative; width: 1200px; height: 786px; }
  .card {
    position: absolute;
    width: 560px; height: 320px;
    background: var(--card-fill);
    border: 12px solid var(--brand-blue);
    box-shadow: 0 18px 40px rgba(0,0,0,0.45);
  }
  .card-front { left: 60px; top: 80px; }
  .card-back { left: 580px; top: 386px; }

  /* front */
  .brand-block {
    position: absolute; left: 34px; top: 0; bottom: 0; width: 210px;
    display: flex; flex-direction: column; justify-content: center;
  }
  .brand-line { display: flex; align-items: center; gap: 10px; }
  .brand-mark { width: 16px; height: 16px; background: var(--brand-blue); flex: none; }
  .brand-name {
    color: var(--brand-blue); font-weight: 600; font-size: 20px;
    letter-spacing: 1px; text-transform: uppercase; line-height: 1.15;
  }
  .brand-rule { margin-top: 10px; width: 190px; height: 1px; background: var(--brand-grey); }
  .divider {
    position: absolute; left: 262px; top: 70px; width: 1px; height: 170px;
    background: var(--brand-blue);
  }
  .contact { position: absolute; left: 286px; top: 62px; color: var(--text-light); }
  .contact-name {
    color: var(--brand-blue); font-weight: 500; font-size: 22px;
    letter-spacing: 1.5px; text-transform: uppercase;
  }
  .contact-role { font-size: 12px; margin: 4px 0 12px; }
  .contact-address { font-size: 12px; line-height: 1.5; margin-bottom: 10px; }
  .contact-row { display: flex; align-items: center; gap: 7px; font-size: 12px; line-height: 1.6; }
  .contact-row svg { width: 11px; height: 11px; flex: none; }

  /* back */
  .back-brand {
    position: absolute; left: 0; right: 0; top: 80px;
    display: flex; justify-content: center; align-items: center; gap: 14px;
  }
  .back-brand .brand-mark { width: 26px; height: 26px; }
  .back-brand .brand-name { font-size: 34px; }
  .services {
    position: absolute; left: 0; right: 0; bottom: 54px;
    text-align: center; color: var(--text-light);
    font-size: 13px; letter-spacing: 0.8px; text-transform: uppercase; line-height: 1.8;
  }
  .services .sep { color: var(--brand-blue); padding: 0 4px; }
</style>
</head>
<body>
<main class="canvas">
  <section class="card card-front">
    <div class="brand-block">
      <div class="brand-line">
        <span class="brand-mark"></span>
        <span class="brand-name">Brightline Works LTD</span>
      </div>
      <div class="brand-rule"></div>
    </div>
    <div class="divider"></div>
    <div class="contact">
      <p class="contact-name">Daniel Hart</p>
      <p class="contact-role">Director</p>
      <p class="contact-address">1420 Alder Court<br>Salem, OR 97301</p>
      <p class="contact-row">
        <svg viewBox="0 0 12 12" aria-hidden="true"><path d="M2.5 1 L4.5 1 L5 3.5 L3.8 4.5 Q5 7 7.5 8.2 L8.5 7 L11 7.5 L11 9.5 Q10.5 11 9 11 Q1 10 1 3 Q1 1.5 2.5 1Z" fill="var(--brand-blue)"/></svg>
        555.204.7318
      </p>
      <p class="contact-row">
        <svg viewBox="0 0 12 12" aria-hidden="true"><rect x="1" y="2.5" width="10" height="7" fill="none" stroke="var(--brand-blue)" stroke-width="1.2"/><path d="M1 2.5 L6 6.5 L11 2.5" fill="none" stroke="var(--brand-blue)" stroke-width="1.2"/></svg>
        hello@brightlineworks.com
      </p>
      <p class="contact-row">
        <svg viewBox="0 0 12 12" aria-hidden="true"><circle cx="6" cy="6" r="5" fill="none" stroke="var(--brand-blue)" stroke-width="1.2"/><ellipse cx="6" cy="6" rx="2.2" ry="5" fill="none" stroke="var(--brand-blue)" stroke-width="1"/><path d="M1 6 H11" stroke="var(--brand-blue)" stroke-width="1"/></svg>
        www.brightlineworks.com
      </p>
    </div>
  </section>

  <section class="card card-back">
    <div class="back-brand">
      <span class="brand-mark"></span>
      <span class="brand-name">Brightline Works</span>
    </div>
    <div class="services">
      <p>Electrical/Site Temporary Electrics</p>
      <p>Data/Network Installation<span class="sep">|</span>Passive Fire Protection</p>
    </div>
  </section>
</main>
</body>
</html>
```